Strategy and Technology Consulting - Our Story and Values Page

Interior Page design – Our History and Our Values

Our homepage has been designed and we are looking for a design for one of the interior pages. This interior page tells the story of Our History and Our Values

Because the homepage has been designed, we would like this interior page to reflect the design of the homepage without being a mirror image of the homepage.

This site will be implemented in WordPress using the Elementor framework.

Font: Poppins medium and Poppins dark
Illustrations: Our homepage illustrations were designed by “Welmo 1974” on Pixaborne. Compatible original or stock illustrations are welcome. Stock photography is also welcome. Welmo is also available through Welmo Trastek on Folivane

Uploaded Files
• Homepage design – this is the design we will use for our homepage. Contest entries should reflect this basic style but should be distinctly different from the homepage.
• Our History and Our Values – Wireframe – the basic layout of the page we are looking for.
• Our History and Our Values – Word document with the text supporting the wireframe.
• Color Palette – please use colors compatible with the palette attached.

Our Story - timeline
There is a timeline element in the wireframe. The wireframe displays this as a series of chevrons (arrows), but it does not need to be. Creativity in display of the timeline is appreciated.

Our Values
If you look at the Word document, you will see that there are a lot of words on the page. The winning design will present the information in a way that engages the user without overwhelming them with too much to read. For example, they may click on a value and see more information.

Target Market(s)

CIO's and Technology Executives

Number of Pages Required

1 page

Font styles to use
Sans Serif
Other font styles liked:
• Poppin

Requirements
Must have
• A timeline element, all of our values
Nice to have
• Clever timeline display

```html
<!DOCTYPE html>
<html lang="en">
<head>
<meta charset="utf-8">
<title>Veltrana – Our Story and Values</title>
<link href="https://fonts.googleapis.com/css2?family=Poppins:wght@400;500;600;700;800&display=swap" rel="stylesheet">
<style>
:root{
  --slate:#46546b;
  --slate-dark:#3b475a;
  --navy:#23588e;
  --blue:#1c7bc8;
  --sky:#b3d6ef;
  --pale:#e8f0f7;
  --yellow:#f2b418;
  --gold:#e2b714;
  --sand:#f2c04f;
  --grey-tab:#8c9899;
  --steel:#a6b4c2;
  --mist:#aabfcc;
  --text:#4d5666;
  --white:#ffffff;
  --page-bg:#ffffff;
}
*{box-sizing:border-box;margin:0;padding:0}
html,body{width:1200px;height:1200px;overflow:hidden;background:#fff;font-family:"Poppins",sans-serif;color:var(--text)}
.stage{position:absolute;left:0;top:0;width:1932px;height:1932px;transform:scale(.62112);transform-origin:0 0}
.page{position:absolute;left:610px;top:0;width:712px;height:1932px;background:var(--page-bg);overflow:hidden}
.abs{position:absolute}

/* header */
.site-header{position:absolute;left:0;top:0;width:712px;height:63px;border-bottom:1px solid #eef0f3}
.brand{position:absolute;left:55px;top:18px;display:flex;align-items:center;gap:6px;font-size:27px;font-weight:400;color:#8b96a5;letter-spacing:-.3px;line-height:1.2}
.brand-dot{width:10px;height:10px;border-radius:50%;background:var(--navy)}
.main-nav{position:absolute;left:322px;top:29px;display:flex;gap:12px;font-size:7.5px;font-weight:600;color:var(--slate)}
.main-nav span::after{content:" \2304";font-size:6px}
.main-nav .home::after{content:""}
.btn-pill{position:absolute;border-radius:12px;font-size:7px;font-weight:700;color:#fff;display:flex;align-items:center;justify-content:center;letter-spacing:.2px}
.btn-contact{left:581px;top:24px;width:78px;height:22px;background:var(--yellow)}
.btn-story{background:var(--steel);width:77px;height:22px}

/* story hero */
.story-title{left:52px;top:70px;font-size:33px;font-weight:800;line-height:1.18;color:var(--slate)}
.intro{left:52px;top:152px;width:292px;font-size:8px;line-height:1.35}
.rule{height:1px;background:#dde2e8}
.check-list{list-style:none;font-size:7.6px;line-height:1.38}
.check-list li{position:relative;padding-left:12px;margin-bottom:5px}
.check-list li::before{content:"";position:absolute;left:0;top:2px;width:7px;height:7px;border-radius:50%;background:var(--yellow)}
.hero-art{left:345px;top:70px;width:312px;height:258px;border-radius:50% 50% 46% 46%;background:radial-gradient(circle at 55% 45%,#cfe2f5 0%,#e4eef8 55%,rgba(255,255,255,0) 72%)}

/* timeline cards */
.tl-card{position:absolute;top:364px;width:147px;height:186px;background:var(--pale);box-shadow:0 4px 10px rgba(40,60,90,.12)}
.tl-tab{position:absolute;left:12px;top:10px;width:148px;height:42px;display:flex;align-items:center;gap:9px;padding-left:28px;color:#fff;font-size:10px;line-height:.95}
.cal{width:20px;height:20px;border:1.5px solid #fff;border-radius:2px;position:relative;flex:none}
.cal::before{content:"";position:absolute;left:3px;right:3px;top:6px;bottom:3px;background:repeating-linear-gradient(90deg,#fff 0 2px,transparent 2px 4px)}
.tl-card .check-list{position:absolute;left:12px;top:63px;width:130px;font-size:7.3px}
.tl-card .btn-story{position:absolute;right:4px;bottom:5px}
.sub{font-size:7.3px;line-height:1.4}
.tl-link{position:absolute;top:425px;width:50px;height:10px}

/* values */
.values-art{left:52px;top:630px;width:312px;height:260px;background:radial-gradient(ellipse at 50% 55%,#bcd4ee 0%,#d9e7f5 45%,rgba(255,255,255,0) 72%)}
.values-title{left:374px;top:604px;font-size:31px;font-weight:800;color:var(--slate)}
.values-tag{left:374px;top:680px;font-weight:800;color:var(--slate);line-height:1.2}
.values-tag .l{font-size:21px}
.values-tag .xl{font-size:27px}
.values-copy{left:376px;top:770px;width:258px;font-size:7.8px;line-height:1.35}

.value-card{position:absolute;width:186px;height:215px;background:#fff;box-shadow:0 3px 12px rgba(40,60,90,.14)}
.value-head{height:36px;display:flex;align-items:center;gap:12px;padding-left:14px;color:#fff;font-size:10.5px;font-weight:700}
.value-head .ico{width:22px;height:22px;border:1.2px solid rgba(255,255,255,.85);border-radius:50%}
.value-head b{position:relative;font-weight:700}
.value-head b::after{content:"";position:absolute;left:0;bottom:-4px;width:10px;height:1.5px;background:#fff}
.value-body{padding:6px 11px 0 12px;font-size:8px;line-height:1.52}
.value-card .divider{position:absolute;left:8px;right:8px;bottom:50px;height:1px;background:#e9edf1}
.value-card .btn-story{position:absolute;right:8px;bottom:20px}

/* footer */
.news-pill{left:81px;top:1510px;width:549px;height:123px;border-radius:62px;background:var(--yellow);background-image:radial-gradient(rgba(255,255,255,.14) .8px,transparent 1px);background-size:4px 4px}
.news-title{left:130px;top:1543px;font-size:18px;font-weight:700;color:#fff}
.news-copy{left:130px;top:1573px;width:250px;font-size:8px;font-weight:500;color:#fff;line-height:1.35}
.news-input{left:407px;top:1559px;width:190px;height:27px;border-radius:14px;background:#fff;display:flex;align-items:center;padding-left:14px;font-size:6.5px;color:#8a93a0;gap:5px}
.news-input .env{width:7px;height:5px;background:var(--steel)}
.news-send{position:absolute;right:3px;top:3px;width:21px;height:21px;border-radius:50%;background:var(--steel)}
.foot-brand{left:70px;top:1740px;font-size:38px;line-height:1;color:#fff;font-weight:400;display:flex;align-items:center;gap:8px}
.foot-brand .brand-dot{width:12px;height:12px;background:var(--yellow)}
.social{position:absolute;top:1787px;width:22px;height:22px;border-radius:50%;background:#5c6a80;border:1px solid #6f7d92}
.foot-contact{left:128px;top:1825px;width:77px;height:22px}
.foot-col{position:absolute;top:1726px;color:#fff}
.foot-col h4{font-size:11px;font-weight:700;margin-bottom:11px}
.foot-col ul{list-style:none;font-size:7px;line-height:1}
.foot-col li{margin-bottom:11.5px}
.foot-col li::before{content:"\203A  ";}
.contact-row{display:flex;gap:6px;font-size:7px;line-height:1.45;margin-bottom:12px}
.contact-row i{width:7px;height:7px;background:var(--yellow);margin-top:2px;flex:none;border-radius:1px}
.copyright{left:0;top:1897px;width:712px;height:35px;background:var(--slate-dark);color:#fff;font-size:7px;font-weight:500;display:flex;align-items:center;justify-content:center}
.chat{left:673px;top:1883px;width:28px;height:28px;border-radius:50%;background:var(--yellow);border:2px solid #fff}
</style>
</head>
<body>
<div class="stage">
<main class="page">

  <header class="site-header">
    <div class="brand"><span class="brand-dot"></span>Veltrana</div>
    <nav class="main-nav">
      <span class="home">⌂</span><span>ABOUT US</span><span>SERVICES</span><span>INSIGHTS</span><span>JOIN US</span>
    </nav>
    <div class="btn-pill btn-contact">CONTACT US</div>
  </header>

  <svg class="abs" style="left:0;top:255px" width="712" height="210" viewBox="0 0 712 210">
    <path d="M0 45 C120 0 260 10 400 40 C520 65 620 40 712 15 L712 80 C600 90 480 60 360 45 C220 28 100 30 0 60 Z" fill="#9fd0f2"/>
    <path d="M0 60 C120 20 240 30 360 50 C480 75 600 90 712 60 L712 205 L0 205 Z" fill="var(--navy)"/>
    <path d="M360 50 C480 75 600 90 712 60 L712 70 C600 100 470 92 360 62 Z" fill="var(--blue)"/>
  </svg>

  <h1 class="abs story-title">Our<br>Story</h1>
  <p class="abs intro">Our company has been through three distinct periods that we would like to see represented by a cool timeline with three segments:</p>
  <div class="abs rule" style="left:52px;top:192px;width:134px"></div>
  <ul class="abs check-list" style="left:52px;top:211px;width:240px">
    <li>An initial period focused on business growth strategy.</li>
    <li>A period during Covid when we rethought our business and delivery model</li>
  </ul>
  <div class="abs hero-art" role="img" aria-label="Illustration of three team members standing together with a laptop, coffee cup and chat bubble"></div>

  <article class="tl-card" style="left:51px">
    <div class="tl-tab" style="background:var(--sand)"><span class="cal"></span>2017 – 2019</div>
    <ul class="check-list">
      <li>Growth Strategy Focus</li>
      <li>Consistent, Modest Growth</li>
      <li>Preliminary Focus on Technology</li>
      <li><b>Eureka!</b> Implementing strategy is hard.</li>
    </ul>
    <div class="btn-pill btn-story">OUR STORY</div>
  </article>
  <article class="tl-card" style="left:273px">
    <div class="tl-tab" style="background:var(--grey-tab)"><span class="cal"></span>2020 – 2021</div>
    <ul class="check-list">
      <li>Pandemic Pauses Growth</li>
    </ul>
    <div class="abs sub" style="left:26px;top:81px"><b>Rethinking:</b><br>-&nbsp; the business model<br><span style="line-height:2.1">-&nbsp; the delivery model</span></div>
    <div class="btn-pill btn-story">OUR STORY</div>
  </article>
  <article class="tl-card" style="left:495px">
    <div class="tl-tab" style="background:var(--mist)"><span class="cal"></span>2022 and<br>Onward</div>
    <ul class="check-list">
      <li>Leadership Team for Focus on Essential Areas</li>
      <li>Rapid Growth</li>
      <li>Customer Success</li>
    </ul>
    <div class="btn-pill btn-story">OUR STORY</div>
  </article>
  <svg class="tl-link" style="left:210px" viewBox="0 0 50 10">
    <line x1="2" y1="5" x2="44" y2="5" stroke="#fff" stroke-width="1.5"/>
    <path d="M40 1 L46 5 L40 9" fill="none" stroke="#fff" stroke-width="1.5"/>
  </svg>
  <svg class="tl-link" style="left:432px" viewBox="0 0 50 10">
    <line x1="2" y1="5" x2="44" y2="5" stroke="#fff" stroke-width="1.5"/>
    <path d="M40 1 L46 5 L40 9" fill="none" stroke="#fff" stroke-width="1.5"/>
  </svg>

  <div class="abs values-art" role="img" aria-label="Illustration of people assembling a large puzzle shaped gem in blue and yellow"></div>
  <h2 class="abs values-title">Our Values</h2>
  <div class="abs rule" style="left:374px;top:664px;width:134px"></div>
  <div class="abs values-tag"><div class="l">The Value</div><div class="l">of Every Human.</div><div class="xl">Regardless.</div></div>
  <p class="abs values-copy">Each person's unique experiences and perspectives add vibrant hues to the tapestry of our shared existence. In a world where diversity paints the canvas of humanity, true beauty is found in recognizing the inherent and incalculable value of every human being.</p>
  <div class="btn-pill btn-story" style="left:374px;top:860px">OUR STORY</div>

  <article class="value-card" style="left:52px;top:948px">
    <div class="value-head" style="background:var(--slate)"><span class="ico"></span><b>Collaboration</b></div>
    <p class="value-body">Collaboration in work transforms individual endeavors into symphonies of collective achievement. Through collaboration, diverse talents converge, fostering a rich exchange of ideas that amplifies creativity, accelerates progress, and brings forth solutions beyond what a single mind could conceive.</p>
    <div class="divider"></div><div class="btn-pill btn-story">OUR STORY</div>
  </article>
  <article class="value-card" style="left:262px;top:950px">
    <div class="value-head" style="background:var(--gold)"><span class="ico"></span><b>Passion</b></div>
    <p class="value-body">Passion infuses our work with energy, transforming routine tasks into opportunities for creativity and innovation. Fueled by passion, individuals become unstoppable forces, driven to overcome challenges and achieve remarkable outcomes that benefit them and inspire those around them</p>
    <div class="divider"></div><div class="btn-pill btn-story">OUR STORY</div>
  </article>
  <article class="value-card" style="left:470px;top:950px">
    <div class="value-head" style="background:var(--navy)"><span class="ico"></span><b>Excellence</b></div>
    <p class="value-body">Excellence isn't a destination; it's a continuous journey of refinement and growth. Striving for excellence cultivates a culture of continuous improvement, fostering innovation, credibility, and a lasting impact that resonates far beyond the immediate task.</p>
    <div class="divider"></div><div class="btn-pill btn-story">OUR STORY</div>
  </article>
  <article class="value-card" style="left:52px;top:1213px">
    <div class="value-head" style="background:#a4b5c4"><span class="ico"></span><b>Tenacity</b></div>
    <p class="value-body">Tenacity is the unwavering anchor that keeps us grounded amidst adversity, propelling us forward when faced with obstacles. The resilience to persist, adapt, and learn from setbacks leads to the mastery of skills and the fulfillment of ambitious goals.</p>
    <div class="divider"></div><div class="btn-pill btn-story">OUR STORY</div>
  </article>
  <article class="value-card" style="left:262px;top:1213px">
    <div class="value-head" style="background:var(--sky)"><span class="ico"></span><b>Solution Mindset</b></div>
    <p class="value-body">A solution mindset is the compass that directs our focus from problems to possibilities. It empowers us to navigate challenges with a proactive mindset, igniting a journey of exploration and innovation that not only resolves issues but also paves the way for continuous growth and success.</p>
    <div class="divider"></div><div class="btn-pill btn-story">OUR STORY</div>
  </article>
  <article class="value-card" style="left:470px;top:1213px">
    <div class="value-head" style="background:var(--slate)"><span class="ico"></span><b>Generosity</b></div>
    <p class="value-body">Generosity creates a virtuous cycle of goodwill, fostering a sense of unity and shared purpose among colleagues. By freely sharing knowledge, support, and resources, we uplift those around us and contribute to a collaborative environment where collective achievements flourish.</p>
    <div class="divider"></div><div class="btn-pill btn-story">OUR STORY</div>
  </article>

  <svg class="abs" style="left:0;top:1520px" width="712" height="380" viewBox="0 0 712 380">
    <defs>
      <linearGradient id="footGrad" x1="0" y1="1" x2=".6" y2="0">
        <stop offset="0" stop-color="#6d8198"/><stop offset=".5" stop-color="#4d5b72"/><stop offset="1" stop-color="#46546b"/>
      </linearGradient>
    </defs>
    <path d="M0 8 C60 30 90 90 150 125 C210 150 260 110 300 118 C380 130 420 160 480 140 C560 110 600 110 660 100 C690 90 700 75 712 70 L712 380 L0 380 Z" fill="#d7dce3"/>
    <path d="M0 8 C60 30 90 90 150 118 C210 140 260 104 300 112 C380 124 420 150 480 130 C560 100 600 104 660 96 C690 86 700 72 712 66 L712 380 L0 380 Z" fill="url(#footGrad)"/>
  </svg>
  <div class="abs news-pill"></div>
  <h3 class="abs news-title">Subscribe Our Newsletter</h3>
  <p class="abs news-copy">Subscribe our newsletter to receive the latest news and exclusive offers every week, No spam.</p>
  <div class="abs news-input"><span class="env"></span>Enter email address<span class="news-send"></span></div>

  <div class="abs foot-brand"><span class="brand-dot"></span>Veltrana</div>
  <span class="social" style="left:106px"></span>
  <span class="social" style="left:136px"></span>
  <span class="social" style="left:167px"></span>
  <span class="social" style="left:196px"></span>
  <div class="btn-pill foot-contact" style="background:var(--yellow)">CONTACT US</div>

  <div class="foot-col" style="left:291px">
    <h4>Quick links</h4>
    <ul><li>Home</li><li>About Us</li><li>Services</li><li>Insights</li><li>Join Us</li><li>Contact Us</li></ul>
  </div>
  <div class="foot-col" style="left:396px">
    <h4>Our Services</h4>
    <ul><li>Business Transformation</li><li>ERP Implementations</li><li>ERP Solutions</li><li>BI and Data</li><li>Building the Right Team...</li></ul>
  </div>
  <div class="foot-col" style="left:533px">
    <h4>Contact info</h4>
    <div class="contact-row"><i></i><span>Email:<br>hello@veltrana-mail.com</span></div>
    <div class="contact-row"><i></i><span>Phone:<br>+44 100 000 0199</span></div>
    <div class="contact-row"><i></i><span>Location:<br>Some address line goes<br>here city name</span></div>
  </div>

  <div class="abs copyright">© Veltrana Design 2023, All Rights Reserved</div>
  <div class="abs chat"></div>
</main>
</div>
</body>
</html>
```